New Website Deisgn. Guaranteed Project.

I would like a site similar to this: http://givebikeforhope.org.

old site: http://wheelsforrelief.org

Create a professional website; a car donation site seeking leads to return calls.

Please see http://givebikeforhope.org for the concept I am after.

The webpage should have a professional feel. The pages to include are 'Home', 'About us' and 'Get Started'

Industry/Entity Type

It Professional

Coding

Coded - Design and coding required

Number of Pages Required

1 page

```html
<!DOCTYPE html>
<html lang="en">
<head>
<meta charset="utf-8">
<title>Wheels for Relief — Donate Your Car</title>
<link href="https://fonts.googleapis.com/css2?family=Fira+Sans+Condensed:wght@400;500;600&family=Open+Sans:wght@400;600;700&display=swap" rel="stylesheet">
<style>
:root{
  --red:#d23a40;
  --red-deep:#b8323a;
  --purple:#33203f;
  --purple-mid:#4a3358;
  --ink:#262633;
  --muted:#5a5a66;
  --line:#cfcfd6;
  --paper:#ffffff;
  --mist:#f1f1f3;
  --field:#ffffff;
}
*{box-sizing:border-box;margin:0;padding:0}
html,body{width:1200px;height:2826px;overflow:hidden;background:var(--paper)}
body{font-family:"Open Sans",Arial,sans-serif;color:var(--ink);position:relative}
.head-font{font-family:"Fira Sans Condensed","Arial Narrow",sans-serif}
section,header,footer{position:absolute;left:0;width:1200px}

/* header */
.site-header{top:0;height:180px;background:var(--paper)}
.brand{position:absolute;left:46px;top:108px;font-family:"Fira Sans Condensed",sans-serif;font-weight:600;font-size:34px;color:var(--red)}
.tagline{position:absolute;left:500px;top:44px;width:370px;text-align:right;color:var(--red);font-weight:700;font-size:16px;line-height:22px}
.call{position:absolute;left:892px;top:40px;display:flex;align-items:center;gap:12px}
.call-label{font-weight:700;font-size:17px;color:var(--purple);line-height:20px}
.call-number{font-weight:700;font-size:28px;color:var(--red);line-height:30px}
.main-nav{position:absolute;left:467px;top:112px;width:733px;height:36px;background:var(--purple);display:flex}
.main-nav a{color:#fff;text-decoration:none;font-weight:700;font-size:15px;line-height:36px;padding:0 26px}
.main-nav a.is-active{background:var(--red)}
.main-nav a:nth-child(2){padding:0 32px}

/* hero */
.hero{top:180px;height:490px}
.hero-photo{position:absolute;inset:0;background:linear-gradient(180deg,#c5dbe8 0%,#e3ecef 45%,#f6f6f6 75%,#e9e9ea 100%)}
.hero-people{position:absolute;left:40px;top:20px;width:440px;height:470px;background:radial-gradient(ellipse at 55% 45%,#d9b79a 0%,#c9a27f 35%,#6fb64d 70%,rgba(111,182,77,0) 72%)}
.hero-cars{position:absolute;left:420px;top:200px;width:420px;height:280px;background:radial-gradient(ellipse at 40% 60%,#d8d8d8 0%,#a9aaac 40%,rgba(200,40,40,.0) 70%),radial-gradient(ellipse at 85% 70%,#c8242b 0%,rgba(200,36,43,0) 45%)}
.hero-title{position:absolute;left:424px;top:62px;font-family:"Fira Sans Condensed",sans-serif;color:var(--red);line-height:1.05}
.hero-title .small{font-size:31px;font-weight:500;display:block}
.hero-title .big{font-size:44px;font-weight:500;display:block}
.donate-card{position:absolute;left:795px;top:8px;width:356px;height:452px}
.donate-card svg{position:absolute;inset:0}
.donate-intro{position:absolute;left:20px;top:48px;width:316px;text-align:center;color:#fff;font-weight:700;font-size:17px;line-height:23px}
.donate-form{position:absolute;left:18px;top:146px;width:320px;display:grid;grid-template-columns:1fr 1fr;gap:11px 16px}
.donate-form .field{height:30px;background:var(--field);border-radius:4px;font-size:12px;color:#8a8a92;line-height:30px;padding-left:10px}
.donate-form .wide{grid-column:1 / 3}
.donate-btn{position:absolute;left:18px;top:380px;width:320px;height:48px;background:var(--purple);color:#fff;font-weight:700;font-size:18px;text-align:center;line-height:48px;border-radius:4px}
.hero-rule{position:absolute;left:392px;top:484px;width:414px;height:6px;background:var(--red)}

/* how it works */
.how{top:670px;height:350px;background:var(--paper)}
.section-title{position:absolute;left:0;width:1200px;text-align:center;font-family:"Fira Sans Condensed",sans-serif;font-weight:500}
.how .section-title{top:58px;font-size:34px;color:var(--red)}
.step{position:absolute;top:130px;width:340px}
.step svg{position:absolute;left:0;top:0}
.step-body{position:absolute;left:84px;top:40px;width:280px}
.step h3{color:var(--red);font-weight:700;font-size:17px;line-height:20px}
.step p{font-size:12.5px;font-weight:600;line-height:16px;color:var(--ink)}
.step ul{list-style:none;margin-top:12px;font-size:12.5px;font-weight:600;line-height:16px}

/* charities */
.charities{top:1020px;height:370px;background:linear-gradient(90deg,#f7f7f8,#ececee)}
.charities .top-rule{position:absolute;left:392px;top:0;width:414px;height:6px;background:var(--red-deep)}
.charities .section-title{top:64px;font-size:34px;color:var(--purple-mid);width:800px}
.partner{position:absolute;left:56px;top:130px;display:flex;align-items:center;gap:14px}
.partner-name{font-family:"Fira Sans Condensed",sans-serif;font-size:27px;color:var(--purple-mid);line-height:29px}
.charity-text{position:absolute;left:428px;top:138px;width:366px;font-size:13.5px;line-height:20px;color:var(--muted)}
.child-photo{position:absolute;left:810px;top:8px;width:380px;height:362px;background:radial-gradient(ellipse at 50% 45%,#ecd2c0 0%,#dcbba6 35%,#e9e9ea 62%)}

/* tax */
.tax{top:1390px;height:632px;background:linear-gradient(180deg,#3c2742 0%,#4b3448 50%,#3a2a40 100%)}
.tax .section-title{top:66px;font-size:34px;color:#fff}
.tax-sub{position:absolute;top:112px;width:1200px;text-align:center;color:#fff;font-size:13.5px;font-weight:700}
.tax-card{position:absolute;top:172px;width:350px;height:370px;background:rgba(190,40,48,.82);border:2px solid #fff;border-radius:8px}
.tax-pill{position:absolute;left:50%;transform:translateX(-50%);top:14px;background:#fff;color:var(--red);font-weight:700;font-size:13.5px;padding:6px 14px;border-radius:6px;white-space:nowrap}
.tax-card p{position:absolute;left:22px;top:74px;width:306px;color:#fff;font-size:12.5px;line-height:18px}
.tax-card p + p{top:164px}
.tax-badge{position:absolute;left:50%;bottom:-48px;transform:translateX(-50%);width:96px;height:96px;border-radius:50%;background:#fff;border:3px solid var(--red);display:flex;flex-direction:column;align-items:center;justify-content:center;color:var(--red);font-weight:700;font-size:12px}
.tax .bottom-rule{position:absolute;left:392px;bottom:-6px;width:414px;height:6px;background:var(--purple)}

/* faq */
.faq{top:2022px;height:544px;background:linear-gradient(90deg,#f6f6f7,#efeff1)}
.faq .section-title{top:64px;font-size:36px;color:var(--purple)}
.faq-list{position:absolute;top:126px;list-style:none;width:414px}
.faq-list li{font-size:13.5px;font-weight:600;line-height:18px;padding:10px 0 9px;border-bottom:1px solid var(--line);color:var(--ink)}
.faq-list li::before{content:"+ ";font-weight:700}

/* footer */
.site-footer{top:2566px;height:214px;background:var(--purple);color:#fff}
.foot-col{position:absolute;top:34px}
.foot-col h4{font-size:13.5px;font-weight:700;color:#c9b8d6;margin-bottom:10px}
.foot-col p,.foot-col li{font-size:12px;line-height:16px;list-style:none}
.foot-flag{position:absolute;left:720px;top:0;width:480px;height:214px;background:linear-gradient(110deg,rgba(51,32,63,1) 0%,rgba(90,60,90,.9) 40%,rgba(150,60,70,.6) 70%,rgba(60,50,90,.8) 100%)}
.foot-brand{position:absolute;left:860px;top:98px;font-family:"Fira Sans Condensed",sans-serif;font-weight:600;font-size:34px;color:var(--red)}
.copyright{position:absolute;top:2780px;left:0;width:1200px;height:46px;text-align:center;font-size:11px;font-weight:600;line-height:46px;color:var(--ink)}
</style>
</head>
<body>

<header class="site-header">
  <div class="brand">Wheels for Relief</div>
  <p class="tagline">Donate Your Car, Truck, RV, Boat, Motorcycle, or ATV in all 50 states and make a difference.</p>
  <div class="call">
    <svg width="44" height="44" viewBox="0 0 44 44" aria-hidden="true"><circle cx="22" cy="22" r="22" fill="#d23a40"/><path d="M15 12c2-1 3 0 4 2l1 3c0 1-1 2-2 3 1 3 4 6 7 7 1-1 2-2 3-2l3 1c2 1 3 2 2 4-1 2-3 3-5 3-8-1-15-8-16-16 0-2 1-4 3-5z" fill="#fff"/></svg>
    <div>
      <div class="call-label">CALL TODAY TO DONATE</div>
      <div class="call-number">1-800-555-0142</div>
    </div>
  </div>
  <nav class="main-nav">
    <a class="is-active" href="#">HOME</a>
    <a href="#">HOW IT WORKS</a>
    <a href="#">ABOUT US</a>
    <a href="#">FAQ</a>
    <a href="#">GET STARTED</a>
  </nav>
</header>

<section class="hero">
  <div class="hero-photo" role="img" aria-label="Hazy city skyline sketch behind a donated pickup truck and classic red car"></div>
  <div class="hero-people" role="img" aria-label="Smiling mother hugging her young daughter"></div>
  <div class="hero-cars" role="img" aria-label="Silver pickup truck and red classic car"></div>
  <h1 class="hero-title"><span class="small">Donate Your Car to Fight</span><span class="big">Children's Cancer</span></h1>
  <div class="donate-card">
    <svg width="356" height="452" viewBox="0 0 356 452" aria-hidden="true"><path d="M0 30 Q0 22 10 20 Q90 8 178 22 Q266 36 346 6 Q356 2 356 14 V452 H0 Z" fill="#d23a40"/></svg>
    <p class="donate-intro">Donating is Easy &amp; Makes a Real Difference. Fill out the form below to instantly donate online.</p>
    <div class="donate-form">
      <div class="field">First Name</div><div class="field">Last Name</div>
      <div class="field wide">Phone Number</div>
      <div class="field wide">Email Address</div>
      <div class="field">Choose Year</div><div class="field">Choose Make</div>
      <div class="field">Vehicle Model</div><div class="field">Zip Code</div>
    </div>
    <div class="donate-btn">Click to Donate your Car</div>
  </div>
  <div class="hero-rule"></div>
</section>

<section class="how">
  <h2 class="section-title">How It Works</h2>
  <div class="step" style="left:66px">
    <svg width="70" height="90" viewBox="0 0 70 90" aria-hidden="true" fill="#33203f"><rect x="6" y="4" width="10" height="8"/><rect x="22" y="4" width="44" height="8"/><rect x="6" y="22" width="10" height="8"/><rect x="22" y="22" width="44" height="8"/><rect x="6" y="40" width="10" height="8"/><rect x="22" y="40" width="30" height="8"/><path d="M10 56 L30 64 L22 68 L30 80 L26 82 L18 70 L12 76 Z"/></svg>
    <div class="step-body">
      <h3>1. Fill out the simple form</h3>
      <p>Use our online vehicle donation form to submit your information.</p>
      <ul><li>- Donating your vehicle is easy</li><li>- Vehicle donations accepted nationwide</li></ul>
    </div>
  </div>
  <div class="step" style="left:433px">
    <svg width="90" height="80" viewBox="0 0 90 80" aria-hidden="true" fill="#33203f"><rect x="4" y="24" width="40" height="26"/><rect x="8" y="28" width="14" height="10" fill="#fff"/><path d="M44 36 L80 20 L82 26 L46 44 Z"/><circle cx="16" cy="54" r="8"/><circle cx="36" cy="54" r="8"/><circle cx="16" cy="54" r="3" fill="#fff"/><circle cx="36" cy="54" r="3" fill="#fff"/></svg>
    <div class="step-body">
      <h3>2. Schedule your free pick-up</h3>
      <p>We will arrange to pick up your vehicle when it is most convenient for you.</p>
      <ul><li>- Any vehicle is accepted</li><li>- Free towing for your charity vehicle donation with 24 hours</li></ul>
    </div>
  </div>
  <div class="step" style="left:838px">
    <svg width="70" height="90" viewBox="0 0 70 90" aria-hidden="true" fill="none" stroke="#33203f" stroke-width="3"><rect x="14" y="4" width="40" height="56"/><rect x="6" y="12" width="40" height="56" fill="#fff"/><text x="14" y="40" font-size="16" fill="#33203f" stroke="none" font-family="Open Sans,sans-serif" font-weight="700">$</text><path d="M28 26 H40 M28 36 H40 M14 50 H40 M14 58 H34"/></svg>
    <div class="step-body">
      <h3>3. Receive tax deduction</h3>
      <p>Once the vehicle donation is complete, you will receive your tax deductable vehicle donation receipt.</p>
    </div>
  </div>
</section>

<section class="charities">
  <div class="top-rule"></div>
  <h2 class="section-title" style="left:200px">Charities We Work With</h2>
  <div class="partner">
    <svg width="120" height="110" viewBox="0 0 120 110" aria-hidden="true"><rect x="0" y="0" width="120" height="110" rx="10" fill="#8fb653"/></svg>
    <div class="partner-name">Bright Future<br>Kids<br>Foundation</div>
  </div>
  <p class="charity-text">Bright Future Kids Foundation's mission is to make a positive difference in the lives of children and their families affected by cancer, by helping people with limited finances and special needs receive funds to assist in meeting their financial needs and to reduce the stress and strain that managing cancer can cause. BFKF also provides funding toward research for children's cancers as well as fosters health wellness and a whole-body approach to cancer treatment and recovery.</p>
  <div class="child-photo" role="img" aria-label="Young child in treatment looking up hopefully"></div>
</section>

<section class="tax">
  <h2 class="section-title">Tax Deduction Information For Your Car Donation</h2>
  <p class="tax-sub">The IRS has set the rules for the tax deduction of your vehicle donation</p>
  <div class="tax-card" style="left:51px">
    <div class="tax-pill">If Your Car Donation Sells for $500 Or Less</div>
    <p>You can claim the fair market value of your vehicle up to and including $500, or the amount it is sold for if less than fair market value.</p>
    <p style="top:142px">When you donate your car, you will receive a tax deductible receipt to be submitted with your taxes.</p>
    <div class="tax-badge"><span>$500 or Less</span><svg width="40" height="14" viewBox="0 0 40 14" aria-hidden="true"><path d="M2 10 L6 4 H30 L38 8 V11 H2 Z" fill="#d23a40"/></svg></div>
  </div>
  <div class="tax-card" style="left:426px">
    <div class="tax-pill">If Your Car Donation Sells for $501 Or More</div>
    <p>You can claim the exact amount for which the vehicle is sold. When you donate your car, we will provide you with a tax deductible receipt.</p>
    <p style="top:142px">Within 30 days from the sale of your vehicle we will provide you with a 1098-C form to submit with your taxes.</p>
    <div class="tax-badge"><span>$501 or More</span><svg width="40" height="14" viewBox="0 0 40 14" aria-hidden="true"><path d="M2 10 L6 4 H30 L38 8 V11 H2 Z" fill="#d23a40"/></svg></div>
  </div>
  <div class="tax-card" style="left:799px">
    <div class="tax-pill">How to File Your Taxes</div>
    <p>To receive a tax deduction for a donated vehicle, you must include any charitable contributions itemized on Schedule A of Form 1040 from the IRS. Include your Wheels for Relief tax-deductible receipt with your tax return. You do not need to submit Form 1098-C if your vehicle sells for less than $500 as your official Wheels for Relief receipt is considered sufficient documentation by the IRS. If your vehicle sells for more than $500 but less than $5,000 you will need to submit the provided 1098-C form along with form 8283.</p>
    <div class="tax-badge"><svg width="44" height="38" viewBox="0 0 44 38" aria-hidden="true"><path d="M2 14 L22 2 L42 14 V36 H2 Z" fill="#d23a40"/><rect x="10" y="8" width="24" height="16" fill="#fff"/><path d="M2 14 L22 28 L42 14" fill="none" stroke="#fff" stroke-width="2"/></svg></div>
  </div>
  <div class="bottom-rule"></div>
</section>

<section class="faq">
  <h2 class="section-title">Frequently Asked Questions</h2>
  <ul class="faq-list" style="left:98px">
    <li>What types of vehicles can be donated?</li>
    <li>If my vehicle is not running, can I still donate?</li>
    <li>What paperwork do I need to donate my vehicle?</li>
    <li>Is my donated vehicle tax -deductible?</li>
    <li>What areas do you service?</li>
    <li>What documents do I need to donate a car to charity?</li>
    <li>What if the vehicle is not registered in my name?</li>
    <li>There are two people listed on the title, what should I do?</li>
    <li>The Title Is In A Deceased Person's Name. How do I complete The Transfer Of Title?</li>
  </ul>
  <ul class="faq-list" style="left:690px">
    <li>How much will I receive as a tax deduction for my vehicle?</li>
    <li>How do you determine the value of my vehicle?</li>
    <li>When will I receive my tax receipt?</li>
    <li>How do I schedule a pick up?</li>
    <li>Who will pick up my vehicle?</li>
    <li>Do I have to be home when my vehicle is picked up?</li>
    <li>How quickly can my vehicle be picked up?</li>
    <li>Can you pick up my vehicle if it's not at my home?</li>
    <li>What will I receive at time of pick-up?</li>
  </ul>
</section>

<footer class="site-footer">
  <div class="foot-flag" role="img" aria-label="Waving national flag fading into the footer"></div>
  <div class="foot-col" style="left:90px;width:270px">
    <h4>About Wheels for Relief</h4>
    <p>We turn donated cars, trucks and boats into real help for families facing childhood cancer. Every gift is picked up free, handled with care and sold to fund support, comfort and research for kids who need it most.</p>
  </div>
  <div class="foot-col" style="left:400px">
    <h4>Navigation</h4>
    <ul><li>Home</li><li>How It works</li><li>About Us</li><li>Faq</li><li>Get Started</li></ul>
  </div>
  <div class="foot-col" style="left:546px">
    <h4>Contact info</h4>
    <div style="display:flex;gap:10px;font-weight:700;font-size:13px;line-height:17px">
      <svg width="22" height="18" viewBox="0 0 22 18" aria-hidden="true" fill="#fff"><path d="M1 6 Q11 -2 21 6 L18 9 L15 6 H7 L4 9 Z"/><rect x="5" y="9" width="12" height="8" rx="1"/></svg>
      <div>CALL 1-800-555-0142<br>Live Operators Available<br>7 Days A Week</div>
    </div>
  </div>
  <div class="foot-brand">Wheels for Relief</div>
</footer>
<div class="copyright">COPYRIGHT © 2017 WHEELS FOR RELIEF. ALL RIGHTS RESERVED.</div>

</body>
</html>
```